Steel Rebar Fabrication Company needs Facebook Ads & page, Instagram Ads & pages designed.

I want to put out an Instagram, Facebook ad, and LinkedIn campaign out for my new company, Ridgeline Metals Inc. I want the ads to be short but clean, clear and precise. I want our address: 4817 Marlowe Dr. Tsawwassen, BC. I want our hours of operation to be listed 8:00am to 4:00pm Monday to Friday. Product Delivery to your job site or pick up at our yard available. We can cut, bend to custom and standard shapes based upon Canadian CSA Standards. We offer products ranging from 10mm to 35mm diameter Grade 400W rebar. We can bend stirrups, dowels, hairpins; whatever your company needs to complete your product. Whether it is a small project, Tilt Up warehouse, Wood Frame Construction with Concrete parkade foundation; we have the team to meet your needs.
Email address: info@ridgelinemetalsinc.ca
We can service all areas of British Columbia.

Target Market(s)

Construction Company's for homes, condominiums, warehouses, commercial, industrial, and infrastructure projects. As well, as the every day DIY home improvement or renovator.

Industry/Entity Type

Construction

Requirements
Nice to have
• Would like to see a image of the rebar steel that I have provided in the ad. Even if it is in the background with a lower opacity level. Bonus if someone includes any of the movie files I have uploaded.

```html
<!DOCTYPE html>
<html lang="en">
<head>
<meta charset="utf-8">
<title>Ridgeline Metals Inc. – Rebar Fabrication</title>
<link rel="stylesheet" href="https://fonts.googleapis.com/css2?family=Montserrat:wght@300;400;500;700;800&display=swap">
<style>
  :root {
    --red: #c11d2e;
    --ink: #231f20;
    --panel: #222222;
    --white: #ffffff;
    --stone: #8a8e90;
  }
  * { margin: 0; padding: 0; box-sizing: border-box; }
  html, body { width: 1200px; height: 1200px; overflow: hidden; background: var(--white); }
  body { font-family: "Montserrat", Arial, sans-serif; color: var(--ink); }
  .ad { position: relative; width: 1200px; height: 1200px; background: var(--white); overflow: hidden; }
  .abs { position: absolute; }

  .side-accent { left: 881px; top: 0; width: 15px; height: 1200px; background: var(--red); }
  .side-photo { left: 896px; top: 0; width: 304px; height: 1200px;
    background: linear-gradient(180deg, #8d9294 0%, #a7abad 35%, #6e7478 70%, #b9bcbd 100%); }

  .photo { border-radius: 10px; }
  .photo-towers { left: 525px; top: 116px; width: 596px; height: 651px;
    background: linear-gradient(180deg, #5d9fd9 0%, #9cc6ea 45%, #7d97a8 70%, #3f6b3a 100%); }
  .photo-site { left: 525px; top: 786px; width: 290px; height: 162px;
    background: linear-gradient(135deg, #8b8f86 0%, #a98a6a 50%, #6c7a5c 100%); }
  .photo-rebar { left: 832px; top: 786px; width: 289px; height: 162px;
    background: linear-gradient(135deg, #5e4a3a 0%, #8a6a4e 50%, #9aa0a6 100%); }

  .brand { left: 44px; top: 40px; width: 320px; font-weight: 700; color: var(--ink); text-align: center; }
  .brand-name { font-size: 48px; line-height: 1; letter-spacing: 1px; }
  .brand-sub { font-size: 24px; line-height: 1; margin-top: 14px; letter-spacing: 3px; }

  .tagline { left: 44px; top: 191px; font-size: 25px; font-weight: 400; letter-spacing: 9.4px; color: var(--red); white-space: nowrap; }
  .headline { left: 41px; top: 226px; font-size: 64px; font-weight: 800; line-height: 60px; color: var(--red); letter-spacing: 0.5px; }

  .hours-band { left: 0; top: 364px; width: 500px; height: 120px; }
  .hours-label { left: 27px; top: 376px; width: 351px; height: 34px; background: var(--white); border-radius: 3px;
    color: var(--red); font-weight: 700; font-size: 27px; line-height: 34px; padding-left: 17px; }
  .hours-time { left: 44px; top: 410px; color: var(--white); font-size: 33px; font-weight: 700; line-height: 38px; white-space: nowrap; }
  .hours-time .thin { font-weight: 400; }
  .hours-days { left: 44px; top: 448px; color: var(--white); font-size: 28px; font-weight: 400; line-height: 32px; white-space: nowrap; }

  .services { left: 27px; top: 506px; width: 459px; height: 393px; background: var(--panel); border-radius: 24px 24px 0 0; }
  .services-head { left: 38px; top: 515px; width: 431px; height: 48px; background: var(--red); border-radius: 16px 16px 0 0;
    color: var(--white); font-weight: 700; font-size: 26px; line-height: 48px; padding-left: 60px; }
  .service-list { left: 44px; top: 580px; width: 440px; list-style: none; }
  .service-list li { position: relative; padding-left: 32px; color: var(--white); font-size: 17px; line-height: 21px; font-weight: 400; }
  .service-list svg { position: absolute; left: 0; top: 4px; }
  .service-list li + li { margin-top: 23px; }

  .delivery { left: 27px; top: 911px; width: 459px; height: 152px; background: var(--red); border-radius: 6px 6px 24px 24px;
    color: var(--white); font-weight: 700; font-size: 27px; line-height: 30px; text-align: center;
    display: flex; align-items: center; justify-content: center; padding: 0 16px; }

  .coverage { left: 525px; top: 976px; width: 341px; height: 76px; background: var(--panel); border-radius: 8px;
    color: var(--white); font-size: 20px; font-weight: 400; line-height: 24px; text-align: center;
    display: flex; align-items: center; justify-content: center; }
  .coverage strong { color: var(--red); font-weight: 700; }

  .contact-email { left: 48px; top: 1098px; display: flex; align-items: center; gap: 14px; font-size: 20px; font-weight: 400; white-space: nowrap; }
  .contact-divider { left: 444px; top: 1084px; width: 2px; height: 65px; background: var(--ink); }
  .contact-pin { left: 486px; top: 1084px; }
  .contact-address { left: 545px; top: 1079px; font-size: 31px; font-weight: 400; line-height: 44px; white-space: nowrap; }
</style>
</head>
<body>
<div class="ad">
  <div class="abs side-accent"></div>
  <div class="abs side-photo" role="img" aria-label="Close-up of a modern glass and steel building facade"></div>

  <div class="abs brand">
    <div class="brand-name">RIDGELINE</div>
    <div class="brand-sub">METALS INC.</div>
  </div>

  <div class="abs tagline">YOUR CHANCE NOW</div>
  <h1 class="abs headline">BUILD YOUR<br>DREAM</h1>

  <svg class="abs hours-band" viewBox="0 0 500 120" aria-hidden="true">
    <polygon points="0,0 418,0 500,120 0,120" fill="var(--red)"/>
  </svg>
  <div class="abs hours-label">OPERATION HOURS</div>
  <div class="abs hours-time">8:00AM <span class="thin">TO</span> 4:00PM</div>
  <div class="abs hours-days">MONDAY TO FRIDAY</div>

  <div class="abs services"></div>
  <h2 class="abs services-head">OUR SERVICES</h2>
  <ul class="abs service-list">
    <li><svg width="15" height="14" viewBox="0 0 15 14" aria-hidden="true"><rect x="1" y="2" width="11" height="11" fill="none" stroke="var(--red)" stroke-width="1.6"/><path d="M3.5 7 L6.5 10 L14 1.5" fill="none" stroke="var(--red)" stroke-width="1.8"/></svg>We can cut, bend to custom and standard shapes based upon Canadian CSA Standards</li>
    <li><svg width="15" height="14" viewBox="0 0 15 14" aria-hidden="true"><rect x="1" y="2" width="11" height="11" fill="none" stroke="var(--red)" stroke-width="1.6"/><path d="M3.5 7 L6.5 10 L14 1.5" fill="none" stroke="var(--red)" stroke-width="1.8"/></svg>We can bend stirrups, dowels, hairpins; whatever your company needs to complete your product.</li>
    <li><svg width="15" height="14" viewBox="0 0 15 14" aria-hidden="true"><rect x="1" y="2" width="11" height="11" fill="none" stroke="var(--red)" stroke-width="1.6"/><path d="M3.5 7 L6.5 10 L14 1.5" fill="none" stroke="var(--red)" stroke-width="1.8"/></svg>We offer products ranging from 10mm to 35mm diameter Grade 400W rebar.</li>
    <li><svg width="15" height="14" viewBox="0 0 15 14" aria-hidden="true"><rect x="1" y="2" width="11" height="11" fill="none" stroke="var(--red)" stroke-width="1.6"/><path d="M3.5 7 L6.5 10 L14 1.5" fill="none" stroke="var(--red)" stroke-width="1.8"/></svg>Whether it is a small project, Tilt Up warehouse, Wood Frame Construction with Concrete parkade foundation; we have the team to meet your needs.</li>
  </ul>

  <div class="abs delivery">PRODUCT DELIVERY TO YOUR JOB SITE OR PICK UP AT OUR YARD AVAILABLE</div>

  <div class="abs photo photo-towers" role="img" aria-label="City skyline with curved glass towers against a blue sky above green trees"></div>
  <div class="abs photo photo-site" role="img" aria-label="Aerial view of a construction site with rebar laid over a foundation"></div>
  <div class="abs photo photo-rebar" role="img" aria-label="Close-up of a tied steel rebar grid"></div>

  <div class="abs coverage"><p>WE CAN SERVICE ALL AREAS<br>OF <strong>BRITISH COLUMBIA</strong></p></div>

  <div class="abs contact-email">
    <svg width="40" height="29" viewBox="0 0 40 29" aria-hidden="true">
      <rect x="0" y="0" width="40" height="29" rx="3" fill="var(--red)"/>
      <path d="M2 3 L20 16 L38 3" fill="none" stroke="var(--white)" stroke-width="3"/>
    </svg>
    <span>info@ridgelinemetalsinc.ca</span>
  </div>
  <div class="abs contact-divider"></div>
  <svg class="abs contact-pin" width="46" height="58" viewBox="0 0 46 58" aria-hidden="true">
    <path d="M23 2 C13 2 6 9 6 18 C6 30 23 46 23 46 C23 46 40 30 40 18 C40 9 33 2 23 2 Z" fill="var(--red)"/>
    <circle cx="23" cy="18" r="6.5" fill="var(--white)"/>
    <path d="M12 42 C4 44 2 47 2 49 C2 54 12 56 23 56 C34 56 44 54 44 49 C44 47 42 44 34 42" fill="none" stroke="var(--red)" stroke-width="4"/>
  </svg>
  <div class="abs contact-address">4817 Marlowe<br>Dr. Tsawwassen, BC.</div>
</div>
</body>
</html>
```